A new business in the finance sector helping asset managers raise assets needs a basic website.

Marrowgate Partnerships website design brief

SUMMARY
I need a basic website created. The brief includes both designing the website and setting it up via a mainstream website building website like WIX, such that I can edit it and add pages subsequently.

BUSINESS BACKGROUND
Marrowgate Partnerships Limited is a UK Limited company operating in what we can broadly define as finance. The business has been set up to help various asset management companies with asset raising. These companies are good at managing money but not necessarily good at marketing their skills to prospective investors such as: pension funds, endowments, foundations, family offices and private wealth management groups.

Generally, it is likely that I will carry the card of the firms I am representing so Marrowgate Partnerships itself won’t be widely used and, as such, I don’t expect the website to get much traffic but it when people do seek to check it out, it needs to convey an image of trustworthiness and professionalism.

For regulatory reasons I won’t be able to do any marketing on the website so this may well end up as a 1 or 2 page website with an introductory page and a bio on me (plus, in time, any others that I choose to partner with or employ) BUT it may be that I can includes some information on the groups I am working with and so I would like the design to allow for me to add pages easily in the future.

MOOD / DESIGN
Asset raising is an important but serious business: integrity, trust and stability are all key. Investors – and particularly the institutional investors that I be speaking to – don’t want anything flashy or trendy; they are looking to build long term relationships and make long term investments. Trustworthiness, longevity, and professionalism are all key.
I am open minded to a more obvious, tried and tested City/Wall Street type design (cue skyscrapers / London City skyline and serious people around a smart board room table) but also interested to explore something that holds to the same values but is more modern.
One of my two initial clients is focused on environmental investment opportunities and I could imagine the winning design wanting to incorporate some reference to that…..although because other managers I work with are not focused on this area, the design cannot be all about that.

WHAT ARE MARROWGATE PARTNERSHIPS?
A core element of almost any investment strategy – and this is often true in other areas of life too – is to diversify your risk or exposure. In the design world that might mean multiple clients across multiple industries, etc.

In the asset management world (often referred to as money management or fund management), a lot of investments are quite highly correlated, meaning that although they may appear different in some regards, in reality they perform in quite similar ways and especially in times of financial stress such as that experienced in 2007-2009 or, indeed, right now due to Covid.

As such, investors are always interested in finding strategies that offer genuine, reliable diversification where performance is linked to factors unrelated to mainstream financial markets. They may also be interested in some strategies that are negatively correlated to financial markets, meaning they can do well when all around them are doing badly (think of this like having insurance).

Sometimes these strategies offer diversification simply because of what they are invested in (Gold, for example, often does well when stock markets are doing badly as investors seek a safe haven for their money); in other cases it is all about the strategy itself and how it is implemented.
Marrowgate Partnerships is focused on identifying – and marketing - strategies that really are great diversifiers. Very few firms focus on this area so it is a genuine USP.

LOGO?
Logos for my sort of business are generally frowned upon being considered too flashy. As such, I am unlikely to use one……but the nature of the businesses area of focus (see above) does perhaps lend itself to a logo which has some meaning so I am open-minded to this.

DELIVERABLES
• Website design
• Website built using Wix or equivalent with two initial pages and scope for me to add further pages relating to the groups I am working with.

Happy to answer other questions you may have.

Target Market(s)

Institutional investors like pension funds, endowments, foundations, family offices, sovereign wealth funds, multi-asset managers and private wealth managers

Industry/Entity Type

Finance

Contact Information for Business Card

Tobin Creel
Marrowgate Partnerships Limited
Room for telephone number and email address but not address
May need to add regulatory information in due course.

Coding

Coded - Design and coding required

Number of Pages Required

3 page

Font styles to use
Sans Serif

Requirements
Must have
• See project description for mood / design brief. Business is serious: trustworthiness and professionalism are key.
Nice to have
• As per the brief more than one of my clients are in the environmental space so some reference to this would be nice to have....but other clients are not so don't want to give the impression that everything is linked to the environment.
Should not have
• Nothing flashy or gimmicky. The website itself will never be a medium for doing business, rather it is a place people may visit to check me out. They won't spend long there, they key is that the impression they are left with is one of: integrity and professionalism.

```html
<!DOCTYPE html>
<html lang="en">
<head>
<meta charset="utf-8">
<title>Marrowgate Partnerships Limited</title>
<link href="https://fonts.googleapis.com/css2?family=Montserrat:wght@400;500;600;700;800&family=Open+Sans:wght@400;600&display=swap" rel="stylesheet">
<style>
:root{
  --cyan:#1ec3dc;
  --ink:#1d1d1d;
  --text:#555;
  --muted:#888;
  --dark:#121417;
  --footer:#222;
  --white:#fff;
}
*{box-sizing:border-box;margin:0;padding:0}
html,body{width:1200px;height:4196px;overflow:hidden}
body{font-family:"Open Sans",sans-serif;color:var(--text);background:var(--white)}
h1,h2,h3,h4,.nav,.btn{font-family:"Montserrat",sans-serif}
section,header,footer{position:relative;width:1200px;overflow:hidden}
.abs{position:absolute}
p{font-size:13px;line-height:1.75}

/* hero */
.hero{height:650px;background:linear-gradient(180deg,#1c2840 0%,#2a3550 45%,#6a4a3a 75%,#c27a3a 100%)}
.hero-photo{position:absolute;inset:0}
.hero-shade{position:absolute;inset:0;background:linear-gradient(90deg,rgba(10,14,30,.55),rgba(10,14,30,.1))}
.brand{left:88px;top:22px;display:flex;align-items:center;gap:12px}
.brand-mark{width:40px;height:40px;border-radius:50%;background:var(--cyan)}
.brand-name{font-family:"Montserrat",sans-serif;font-weight:700;color:var(--white);font-size:16px;line-height:1.15;width:150px}
.nav{right:88px;top:28px;display:flex;gap:8px;list-style:none}
.nav li{color:var(--white);font-size:14px;font-weight:500;padding:8px 14px}
.nav li.active{background:var(--cyan)}
.hero h1{left:88px;top:172px;width:600px;color:var(--white);font-size:50px;line-height:1.12;font-weight:800}
.hero .tagline{left:88px;top:350px;width:560px;color:var(--white);font-family:"Montserrat",sans-serif;font-weight:600;font-size:19px;line-height:1.3}
.btn{display:inline-block;background:var(--cyan);color:var(--white);font-weight:600;font-size:15px;text-align:center}
.hero .btn{left:88px;top:440px;width:200px;height:44px;line-height:44px;border-radius:22px}

/* about */
.about{height:770px}
.section-label{font-size:26px;font-weight:600;color:var(--ink)}
.about .section-label{left:88px;top:730px;top:80px}
.about-photo{left:88px;top:162px;width:492px;height:508px;background:linear-gradient(135deg,#b9c6cf,#6d7f8c 60%,#3d4a55)}
.about h2{left:640px;top:220px;width:480px;font-size:38px;font-weight:600;color:var(--ink);line-height:1.2}
.about p{left:640px;top:330px;width:480px}
.link{color:var(--cyan);font-size:13px;text-decoration:underline}
.about .link{left:640px;top:594px}

/* services */
.services{height:640px;background:radial-gradient(circle at 70% 40%,#2a2e35,var(--dark) 70%)}
.services h2{left:0;width:1200px;text-align:center;top:90px;font-size:40px;font-weight:600;color:var(--white)}
.services .rule{left:580px;top:148px;width:40px;height:3px;background:var(--white)}
.cards{left:160px;top:160px;display:flex}
.card{width:222px;height:288px;background:#0c0d0f;padding:30px 22px;text-align:center;color:#ccc}
.card.alt{background:var(--cyan);color:var(--white)}
.card svg{width:40px;height:40px}
.card h3{color:var(--white);font-size:20px;font-weight:600;margin-top:14px}
.card .dash{width:20px;height:2px;background:var(--white);margin:10px auto 14px}
.card p{font-size:12px;line-height:1.6}
.services .link{left:0;width:1200px;text-align:center;top:488px}

/* videos */
.videos{height:524px}
.videos h4{left:88px;top:52px;font-size:26px;font-weight:600;color:var(--ink)}
.videos h2{left:88px;top:108px;font-size:38px;font-weight:700;color:var(--ink)}
.thumb{top:172px;width:320px;height:200px}
.thumb .play{position:absolute;left:144px;top:84px;width:32px;height:32px;border-radius:50%;background:rgba(255,255,255,.75)}
.videos .link{left:88px;top:412px}

/* clients */
.clients{height:576px}
.clients-panel{left:0;top:0;width:620px;height:576px;background:var(--cyan)}
.clients-photo{left:620px;top:0;width:580px;height:576px;background:linear-gradient(135deg,#e6ecf1,#9fb4c6 55%,#53708a)}
.clients h2{left:88px;top:86px;width:400px;font-size:46px;line-height:1.15;font-weight:600;color:var(--white)}
.clients p{color:var(--white);left:88px;width:500px}
.arrow{top:270px;width:36px;height:36px;border-radius:50%;background:rgba(255,255,255,.35);display:flex;align-items:center;justify-content:center}

/* articles */
.articles{height:888px}
.articles h2{left:0;width:1200px;text-align:center;top:100px;font-size:44px;font-weight:600;color:var(--ink)}
.articles .rule{left:580px;top:162px;width:40px;height:3px;background:var(--ink)}
.post{top:180px;width:296px;height:508px;background:var(--white);box-shadow:0 2px 14px rgba(0,0,0,.12);padding:14px}
.post-photo{width:268px;height:220px}
.post .tag{color:var(--cyan);font-size:11px;margin-top:16px}
.post h3{font-size:21px;font-weight:700;color:var(--ink);line-height:1.2;margin-top:6px}
.post p{font-size:12px;line-height:1.7;margin-top:14px}
.post .link{display:block;margin-top:22px;font-size:12px}

/* footer */
.site-footer{height:112px;background:var(--footer);color:var(--white);font-size:13px}
.site-footer .col{top:34px;line-height:1.9}
.socials{display:inline-flex;gap:8px;vertical-align:middle;margin-left:8px}
.socials span{width:12px;height:12px;border-radius:50%;background:var(--white)}
.copyright{height:36px;background:var(--white);text-align:center;font-size:10px;line-height:36px;color:#444}
</style>
</head>
<body>

<header class="hero">
  <div class="hero-photo" role="img" aria-label="City skyline of glass skyscrapers at dusk"></div>
  <div class="hero-shade"></div>
  <div class="abs brand"><span class="brand-mark"></span><span class="brand-name">Marrowgate Partnerships Limited</span></div>
  <ul class="abs nav">
    <li class="active">Home</li><li>About Us</li><li>Skills</li><li>Clients</li><li>Blog</li><li>Contact Us</li>
  </ul>
  <h1 class="abs">Welcome To Marrowgate Partnerships Limited</h1>
  <div class="abs tagline">A New Business In The Finance Sector Helping Asset Managers Raise Assets</div>
  <span class="abs btn">Get Started</span>
</header>

<section class="about">
  <h4 class="abs section-label">About Us</h4>
  <div class="abs about-photo" role="img" aria-label="Business team working together at a laptop"></div>
  <h2 class="abs">Marrowgate Partnerships Limited.</h2>
  <p class="abs">Lorem ipsum dolor sit amet, consectetur adipiscing elit, sed do eiusmod tempor incididunt ut labore et dolore magna aliqua. Ut enim ad minim veniam, quis nostrud exercitation ullamco laboris nisi ut aliquip ex ea commodo consequat. Duis aute irure dolor in reprehenderit in voluptate velit esse cillum dolore eu fugiat nulla pariatur. Excepteur sint occaecat cupidatat non proident, sunt in culpa qui officia deserunt mollit anim id est laborum.</p>
  <span class="abs link">Learn More About Us</span>
</section>

<section class="services">
  <h2 class="abs">Services</h2>
  <div class="abs rule"></div>
  <div class="abs cards">
    <div class="card">
      <svg viewBox="0 0 40 40" fill="none" stroke="#fff" stroke-width="2"><path d="M6 34h28M10 30V20M18 30V14M26 30V22M8 16l10-8 8 8 8-8"/></svg>
      <h3>Stocks</h3><div class="dash"></div>
      <p>Lorem ipsum dolor sit amet, consectetur adipiscing elit, sed do eiusmod tempor incididunt ut labore et dolore magna aliqua.</p>
    </div>
    <div class="card alt">
      <svg viewBox="0 0 40 40" fill="none" stroke="#fff" stroke-width="2"><rect x="8" y="6" width="24" height="28" rx="2"/><path d="M13 14h14M13 20h14M13 26h9"/></svg>
      <h3>Bonds</h3><div class="dash"></div>
      <p>Lorem ipsum dolor sit amet, consectetur adipiscing elit, sed do eiusmod tempor incididunt ut labore et dolore magna aliqua.</p>
    </div>
    <div class="card">
      <svg viewBox="0 0 40 40" fill="none" stroke="#fff" stroke-width="2"><path d="M6 34h28M8 16h24L20 7zM11 16v15M17 16v15M23 16v15M29 16v15"/></svg>
      <h3>Realestate</h3><div class="dash"></div>
      <p>Lorem ipsum dolor sit amet, consectetur adipiscing elit, sed do eiusmod tempor incididunt ut labore et dolore magna aliqua.</p>
    </div>
    <div class="card alt">
      <svg viewBox="0 0 40 40" fill="none" stroke="#fff" stroke-width="2"><circle cx="20" cy="20" r="13"/><path d="M20 12v16M24 15h-6a3 3 0 000 6h4a3 3 0 010 6h-6"/></svg>
      <h3>Private Equity</h3><div class="dash"></div>
      <p>Lorem ipsum dolor sit amet, consectetur adipiscing elit, sed do eiusmod tempor incididunt ut labore et dolore magna aliqua.</p>
    </div>
  </div>
  <span class="abs link">Learn More</span>
</section>

<section class="videos">
  <h4 class="abs">Watch Video</h4>
  <h2 class="abs">Lorem ipsum dolor sit amet</h2>
  <div class="abs thumb" style="left:88px;background:linear-gradient(135deg,#d8d2c8,#8a7a6a)" role="img" aria-label="Video still of a person working at a desk"><span class="play"></span></div>
  <div class="abs thumb" style="left:440px;background:linear-gradient(135deg,#e2e6ea,#8c98a4)" role="img" aria-label="Video still of financial charts on paper"><span class="play"></span></div>
  <div class="abs thumb" style="left:788px;background:linear-gradient(135deg,#c9ccd0,#5d646c)" role="img" aria-label="Video still of a calculator and documents"><span class="play"></span></div>
  <span class="abs link">See All My Videos</span>
</section>

<section class="clients">
  <div class="abs clients-panel"></div>
  <div class="abs clients-photo" role="img" aria-label="Hands reviewing financial charts on a tablet"></div>
  <h2 class="abs">Clients Value and Work</h2>
  <p class="abs" style="top:230px">Lorem ipsum dolor sit amet, consectetur adipiscing elit, sed do eiusmod tempor incididunt ut labore et dolore magna aliqua. Ut enim ad minim veniam, quis nostrud exercitation ullamco laboris nisi ut aliquip ex ea commodo consequat. Duis aute irure dolor in reprehenderit in voluptate velit esse cillum dolore eu fugiat nulla pariatur. Excepteur sint occaecat cupidatat non proident, sunt in culpa qui officia deserunt mollit anim id est laborum.</p>
  <p class="abs" style="top:420px">Lorem ipsum dolor sit amet, consectetur adipiscing elit, sed do eiusmod tempor incididunt ut labore et dolore magna aliqua.</p>
  <div class="abs arrow" style="left:16px"><svg width="14" height="14" viewBox="0 0 14 14"><path d="M9 2L4 7l5 5" fill="none" stroke="#fff" stroke-width="2"/></svg></div>
  <div class="abs arrow" style="left:1148px"><svg width="14" height="14" viewBox="0 0 14 14"><path d="M5 2l5 5-5 5" fill="none" stroke="#fff" stroke-width="2"/></svg></div>
</section>

<section class="articles">
  <h2 class="abs">Articles</h2>
  <div class="abs rule"></div>
  <article class="abs post" style="left:128px">
    <div class="post-photo" style="background:linear-gradient(135deg,#8a7f74,#3e3a36)" role="img" aria-label="Colleagues reviewing papers at a table"></div>
    <div class="tag">Market Notes</div>
    <h3>Lorem ipsum dolor sit amet, consectetu</h3>
    <p>Lorem ipsum dolor sit amet, consectetur adipiscing elit, sed do eiusmod tempor incididunt ut labore et dolore magna aliqua.</p>
    <span class="link">Read More</span>
  </article>
  <article class="abs post" style="left:452px">
    <div class="post-photo" style="background:linear-gradient(135deg,#e8ecef,#9aa7b3)" role="img" aria-label="Financial reports and charts on a desk"></div>
    <div class="tag">Fund Insights</div>
    <h3>Lorem ipsum dolor sit amet, consectetu</h3>
    <p>Lorem ipsum dolor sit amet, consectetur adipiscing elit, sed do eiusmod tempor incididunt ut labore et dolore magna aliqua.</p>
    <span class="link">Read More</span>
  </article>
  <article class="abs post" style="left:776px">
    <div class="post-photo" style="background:linear-gradient(135deg,#d9dde0,#6f7a82)" role="img" aria-label="Professional working at a bright office desk"></div>
    <div class="tag">Asset Raising</div>
    <h3>Lorem ipsum dolor sit amet, consectetu</h3>
    <p>Lorem ipsum dolor sit amet, consectetur adipiscing elit, sed do eiusmod tempor incididunt ut labore et dolore magna aliqua.</p>
    <span class="link">Read More</span>
  </article>
</section>

<footer class="site-footer">
  <div class="abs col" style="left:88px">Phone No :<br>+44 20 0000 0000</div>
  <div class="abs col" style="left:500px">Email :<br>info@marrowgate.example</div>
  <div class="abs col" style="left:880px">Marrowgate Partnerships Limited<br>Follow Us : <span class="socials"><span></span><span></span></span></div>
</footer>
<div class="copyright">© Copyright 2020 The Company Name All Right Reserved</div>

</body>
</html>
```